Bref créative
Stationary - Morvane Advisory
Business Card, Letterhead & Pen Design
Professional
Helmut Draven
Director
Address line 1
Address line 2
Address line 3
Address line 4
Post Code
QRP@QRP.example
For the business card I like the idea of front/back designs, where either there is something which joins the front and back or there is a slightly modified logo on the back... You're call, I'm open to anything here, so if you come up with something just try it out, I'll give everyone feedback where possible!
Please don't just stick my logo on a pen and say "hey, here you go...", for the pen design I'm looking for colours etc and where they are placed on the pen too!
Anything you think would look good!
Image file to show the logo
Extra images (inc psds!) for the logo

```html
<!DOCTYPE html>
<html lang="en">
<head>
<meta charset="utf-8">
<title>Morvane Advisory — Business Card</title>
<link rel="stylesheet" href="https://fonts.googleapis.com/css2?family=Arimo:wght@400;700&family=Tinos&display=swap">
<style>
  :root {
    --backdrop: #3a3a3c;
    --card: #ffffff;
    --brand-blue: #1b93c4;
    --brand-blue-deep: #0f6f98;
    --ink: #2b2b2b;
    --rule: #9a9a9a;
    --swoosh-light: #e4e4e4;
    --swoosh-dark: #9c9c9c;
  }
  * { margin: 0; padding: 0; box-sizing: border-box; }
  html, body {
    width: 1200px;
    height: 780px;
    overflow: hidden;
    background: var(--backdrop);
  }
  .business-card {
    position: absolute;
    left: 80px;
    top: 90px;
    width: 1040px;
    height: 600px;
    background: var(--card);
    border-radius: 34px;
    overflow: hidden;
  }
  .brand {
    position: absolute;
    left: 96px;
    top: 92px;
    display: flex;
    align-items: center;
    gap: 26px;
  }
  .brand-dot {
    width: 92px;
    height: 92px;
    border-radius: 50%;
    background: var(--brand-blue);
  }
  .brand-name {
    font-family: "Arimo", Arial, sans-serif;
    font-weight: 400;
    font-size: 74px;
    letter-spacing: -1px;
    color: var(--brand-blue);
  }
  .person {
    position: absolute;
    right: 624px;
    top: 316px;
    text-align: right;
    font-family: "Arimo", Arial, sans-serif;
  }
  .person-name {
    font-weight: 700;
    font-size: 30px;
    color: var(--brand-blue);
  }
  .person-title {
    margin-top: 6px;
    font-size: 20px;
    color: var(--ink);
  }
  .divider {
    position: absolute;
    left: 440px;
    top: 260px;
    width: 2px;
    height: 200px;
    background: var(--rule);
  }
  .contact {
    position: absolute;
    left: 462px;
    top: 262px;
    font-family: "Tinos", "Times New Roman", serif;
    font-size: 22px;
    line-height: 31px;
    color: var(--ink);
    list-style: none;
  }
  .contact li { display: flex; align-items: center; gap: 10px; }
  .contact .address { display: block; margin-bottom: 6px; }
  .contact svg { width: 20px; height: 20px; flex: none; }
  .swoosh {
    position: absolute;
    left: 0;
    top: 0;
    width: 1040px;
    height: 600px;
  }
</style>
</head>
<body>
  <div class="business-card">
    <svg class="swoosh" viewBox="0 0 1040 600" aria-hidden="true">
      <defs>
        <linearGradient id="greyBand" x1="0" x2="1" y1="0" y2="0">
          <stop offset="0" stop-color="var(--swoosh-light)"/>
          <stop offset="0.6" stop-color="var(--swoosh-dark)"/>
          <stop offset="1" stop-color="var(--swoosh-light)"/>
        </linearGradient>
        <linearGradient id="blueBand" x1="0" x2="0" y1="0" y2="1">
          <stop offset="0" stop-color="var(--brand-blue)"/>
          <stop offset="1" stop-color="var(--brand-blue-deep)"/>
        </linearGradient>
      </defs>
      <path d="M0 520 C 280 560, 560 470, 1040 430 L1040 452 C 580 490, 300 580, 0 545 Z" fill="url(#greyBand)"/>
      <path d="M0 566 C 300 596, 600 500, 1040 468 L1040 600 L0 600 Z" fill="url(#blueBand)"/>
    </svg>

    <div class="brand">
      <span class="brand-dot"></span>
      <span class="brand-name">Morvane Advisory</span>
    </div>

    <div class="person">
      <div class="person-name">Helmut Draven</div>
      <div class="person-title">Director</div>
    </div>

    <div class="divider"></div>

    <ul class="contact">
      <li class="address">Unit 48 Harlow Lane,<br>Brenmoor, 5091, Eastvale</li>
      <li>
        <svg viewBox="0 0 20 20"><path d="M5 2 L8 6 L6.5 8 C7.5 10.5 9.5 12.5 12 13.5 L14 12 L18 15 L16 18 C9 18 2 11 2 4 Z" fill="var(--brand-blue)"/></svg>
        07000 555 010
      </li>
      <li>
        <svg viewBox="0 0 20 20"><circle cx="10" cy="10" r="8" fill="none" stroke="var(--brand-blue)" stroke-width="2.4"/><circle cx="10" cy="10" r="3.2" fill="none" stroke="var(--brand-blue)" stroke-width="2.4"/></svg>
        QRP@QRP.example
      </li>
      <li>
        <svg viewBox="0 0 20 20"><circle cx="10" cy="10" r="8" fill="none" stroke="var(--brand-blue)" stroke-width="2"/><ellipse cx="10" cy="10" rx="3.5" ry="8" fill="none" stroke="var(--brand-blue)" stroke-width="1.6"/><line x1="2" y1="10" x2="18" y2="10" stroke="var(--brand-blue)" stroke-width="1.6"/></svg>
        www.QRP.example
      </li>
    </ul>
  </div>
</body>
</html>
```